Dry Cleaners Pick-up & Delivery Service

We are in the need of a post card design to hand out in public focused in our dry-cleaners pick up and delivery business services. The postcard must include a price list of most common items sent to the dry cleaners on a regular basis along with promotional sign-up deals and specials as advertised on our website. The color palette must match our website's color scheme - www.vorqualin.com - we would like to focus on our free pick-up and free delivery service. The hand out post card should look clean, organized and neat, yet modern in style projecting the cleanliness of the clothing articles that our customer let us take care of saving them time while we take care of this errand for them. All new customers receive a free high quality, heavy duty laundry bag with our business information and are encouraged to request for $10 of free dry cleaning on their first order, no strings attached, just for signing up to our service.We strive to please our customers and invest on them to have more free time on their hands, plain and simple. We also offer law enforcement uniform special, as the area we focus our routes is a high law enforcement residential community. The logo is attached and must be visible in the postcard as well as the website address and phone number 305-472-1946 as these are the main contact forms of clients reaching our business. This is home based business, we have a partnership with a dry cleaners business who does all of our route customers' dry cleaning needs. Our business is all about the marketing, sales and networking with corporate businesses. The postcard handout must have designs of both sides of the post card as well. They will not be used for mailing for the moment being, they will be only used to hand out.

Industry/Entity Type

Dry Cleaning

```html
<!DOCTYPE html>
<html lang="en">
<head>
<meta charset="utf-8">
<title>Vorqualin Postcard – Front and Back</title>
<link href="https://fonts.googleapis.com/css2?family=Audiowide&family=Lato:wght@400;700&display=swap" rel="stylesheet">
<style>
:root{
  --green:#6cc04a;
  --green-light:#7fce5c;
  --ink:#222;
  --dark:#2b2b2b;
  --black:#000;
  --white:#fff;
  --stage:#e9e9e9;
  --muted:#555;
}
*{box-sizing:border-box;margin:0;padding:0}
html,body{width:1200px;height:1170px;overflow:hidden;background:var(--stage)}
body{position:relative;font-family:'Lato',sans-serif;color:var(--ink)}
.tech{font-family:'Audiowide',sans-serif}
.card{position:absolute;background:var(--white);overflow:hidden;box-shadow:0 4px 18px rgba(0,0,0,.25)}
.card-front{left:33px;top:40px;width:739px;height:572px}
.card-back{left:385px;top:585px;width:739px;height:573px}

/* front */
.front-photo{position:absolute;left:0;top:0;width:739px;height:510px;
  background:linear-gradient(180deg,#fff 0%,#fff 22%,#dfe8f2 45%,#8fb0d6 75%,#5f86bd 100%)}
.brand{position:absolute;text-align:center;font-weight:700;color:var(--ink)}
.front-brand{left:0;width:739px;top:55px;font-size:64px;letter-spacing:1px}
.front-brand .dot{display:inline-block;width:22px;height:22px;border-radius:50%;background:var(--green);margin-left:12px;vertical-align:middle}
.tagline{position:absolute;text-align:center;color:var(--ink)}
.front-tagline{left:0;width:739px;top:166px;font-size:26px}
.signup{position:absolute;background:var(--dark);color:var(--white);border-radius:6px;text-align:center}
.signup .web{color:var(--green)}
.callbox{position:absolute;background:var(--green);color:var(--white);border-radius:6px;text-align:center}
.callbox .note{color:var(--ink)}
.front-signup{left:190px;top:232px;width:389px;height:78px;padding-top:9px}
.front-signup .head{font-size:24px}
.front-signup .web{font-size:22px;margin-top:2px}
.front-call{left:190px;top:313px;width:389px;height:78px;padding-top:12px}
.front-call .num{font-size:24px}
.front-call .note{font-size:16px;margin-top:2px}
.free-badge{position:absolute;left:560px;top:322px;width:140px;height:140px;border-radius:50%;background:var(--white);box-shadow:4px 4px 0 #9a9a9a}
.free-badge .free{position:absolute;left:12px;top:30px;font-size:24px;color:var(--green)}
.free-badge .bag{position:absolute;left:16px;top:62px;width:38px;height:52px;border-radius:8px;background:linear-gradient(#5fb343,#3f8f2a)}
.free-badge .pd{position:absolute;left:58px;top:68px;font-size:15px;line-height:18px;transform:rotate(-14deg)}
.seal{position:absolute;border-radius:50%;background:var(--black);border:4px solid var(--green)}
.front-seal{left:628px;top:422px;width:84px;height:84px}
.offer{position:absolute;left:195px;top:430px;width:400px;text-align:center;color:var(--white);font-size:22px;line-height:29px}
.offer-dot{position:absolute;left:197px;top:446px;width:56px;height:56px;border-radius:50%;background:var(--green)}
.front-foot{position:absolute;left:0;top:510px;width:739px;height:62px;background:var(--black);color:var(--green);font-size:15px;text-align:center;padding-top:14px;letter-spacing:.5px}

/* back */
.back-brand{left:70px;width:260px;top:38px;font-size:44px}
.back-brand .dot{display:inline-block;width:16px;height:16px;border-radius:50%;background:var(--green);margin-left:8px;vertical-align:middle}
.back-tagline{left:40px;width:300px;top:118px;font-size:17px}
.feature{position:absolute;left:143px;width:290px}
.feature h2{font-family:'Audiowide',sans-serif;font-weight:400;color:var(--green);font-size:17px;line-height:29px;letter-spacing:.5px}
.feature p{font-size:12.5px;line-height:15.5px;margin-top:2px}
.feat-free{top:160px}
.feat-fast{top:283px}
.feat-save{top:381px}
.illus{position:absolute;left:40px;top:175px;width:82px;height:78px;border-radius:8px;background:linear-gradient(135deg,#e8eef5,#5faa45)}
.back-seal{left:38px;top:283px;width:80px;height:80px}
.dollar{position:absolute;left:50px;top:375px;font-size:100px;line-height:110px;color:var(--green);font-weight:400}
.back-signup{left:445px;top:38px;width:256px;height:51px;padding-top:5px}
.back-signup .head{font-size:16px}
.back-signup .web{font-size:14px;margin-top:1px}
.back-call{left:445px;top:92px;width:256px;height:51px;padding-top:7px}
.back-call .num{font-size:16px}
.back-call .note{font-size:11px}
.back-offer{position:absolute;left:445px;top:147px;width:256px;text-align:center;font-size:14px;line-height:18px}
.price-sub{position:absolute;left:450px;top:188px;font-size:6px;color:var(--green);letter-spacing:.3px;width:252px;border-bottom:1px solid #ccc;padding-bottom:2px}
.price-title{position:absolute;left:450px;top:206px;font-size:11px;letter-spacing:.6px;color:var(--muted);width:252px;border-top:1px solid #ddd;padding-top:2px}
.price-col{position:absolute;top:226px;width:112px}
.price-col.left{left:450px}
.price-col.right{left:582px;width:122px}
.item{position:relative;height:22px;font-size:6.5px;line-height:7.5px}
.item.tall{height:32px}
.item .sub{font-size:4.5px;line-height:5.5px;color:var(--muted)}
.item .price{position:absolute;right:0;top:0;width:33px;height:10px;border-radius:5px;background:var(--green);color:var(--ink);font-size:6px;line-height:10px;text-align:center}
.item.special{height:auto;font-size:6.5px;line-height:12px}
.fine{position:absolute;left:450px;top:461px;width:252px;font-size:4.5px;line-height:8px;color:#888}
.more{position:absolute;left:450px;top:490px;width:252px;font-size:10.5px;color:var(--green);letter-spacing:.5px;border-top:1px solid #ccc;padding-top:2px}
.back-foot{position:absolute;left:0;top:510px;width:739px;height:63px;background:var(--black);color:var(--green);font-size:14px;letter-spacing:.5px;padding:17px 0 0 37px}
.back-foot .sep{color:var(--white);margin:0 40px 0 30px}
.notch{position:absolute;left:575px;top:506px;width:0;height:0;border-left:6px solid transparent;border-right:6px solid transparent;border-bottom:6px solid var(--black)}
</style>
</head>
<body>

<section class="card card-front" aria-label="Postcard front">
  <div class="front-photo" role="img" aria-label="Photo of freshly cleaned dress shirts hanging on wooden hangers"></div>
  <div class="brand front-brand">Vorqualin<span class="dot"></span></div>
  <div class="tagline front-tagline">Dry Cleaners Pick-up &amp; Delivery Services, LLC</div>

  <div class="signup front-signup tech">
    <div class="head">Sign-up free!</div>
    <div class="web">www.vorqualin.com</div>
  </div>
  <div class="callbox front-call tech">
    <div class="num">Call 305-472-1946</div>
    <div class="note">next-day service available!</div>
  </div>

  <div class="free-badge">
    <div class="free tech">FREE</div>
    <div class="bag" role="img" aria-label="Green laundry bag illustration"></div>
    <div class="pd">Pick-Up<br>&amp; Delivery</div>
  </div>
  <div class="seal front-seal" role="img" aria-label="Satisfaction guarantee seal"></div>

  <div class="offer-dot"></div>
  <p class="offer">Ask about getting<br>$10 off your first dry-cleaning order!</p>

  <div class="front-foot tech">www.deliveryservice@vorqualin.com</div>
</section>

<section class="card card-back" aria-label="Postcard back">
  <div class="brand back-brand">Vorqualin<span class="back-brand dot" style="position:static"></span></div>
  <div class="tagline back-tagline">Dry Cleaners Pick-up &amp; Delivery Services, LLC</div>

  <div class="illus" role="img" aria-label="Illustration of a delivery man holding folded shirts and a green laundry bag"></div>
  <div class="feature feat-free">
    <h2>Free Pick-up &amp;<br>Delivery Dry-cleaning</h2>
    <p>Our delivery service is FREE of charge, even if it is a next-day service request, all you pay is for your dry cleaning or laundry service.<br>No hidden delivery fees.</p>
  </div>

  <div class="seal back-seal" role="img" aria-label="Satisfaction guarantee seal"></div>
  <div class="feature feat-fast">
    <h2>Fast dependable Service</h2>
    <p>You can rest assured that we will take good care of your items like they were ours! Customer service is at the top of our list and satisfaction is guaranteed!</p>
  </div>

  <div class="dollar">$</div>
  <div class="feature feat-save">
    <h2>Save time and Money</h2>
    <p>We know what it's like to have to deal with your daily errands in your daily life and how extended work hours come into play. Save the hassle of having to drop and pick-up your clothes and let us pamper you a little bit. Enjoy more your well deserved time-off with your family from now on!</p>
  </div>

  <div class="signup back-signup tech">
    <div class="head">Sign-up free!</div>
    <div class="web">www.vorqualin.com</div>
  </div>
  <div class="callbox back-call tech">
    <div class="num">Call 305-472-1946</div>
    <div class="note">next-day service available!</div>
  </div>
  <p class="back-offer">Ask about getting $10 off your first dry-cleaning order!</p>

  <div class="price-sub">MOST COMMON CLOTHING ITEMS</div>
  <div class="price-title">DRY CLEANING PRICING</div>

  <div class="price-col left">
    <div class="item">Women Dress<div class="sub">Dry-Cleaned and Pressed -<br>Subject to surcharge (beads, etc)</div><span class="price">$10.95</span></div>
    <div class="item">Women Blouse<div class="sub">Dry-Cleaned and Pressed</div><span class="price">$4.95</span></div>
    <div class="item">Women Casual Pants/<br>Jeans <span class="sub">Dry-Cleaned &amp; Pressed</span><span class="price">$4.95</span></div>
    <div class="item">Skirt - Long<div class="sub">Dry-Cleaned and Pressed</div><span class="price">$6.49</span></div>
    <div class="item">Skirt - Short<div class="sub">Dry-Cleaned and Pressed</div><span class="price">$4.95</span></div>
    <div class="item">Women Suit<div class="sub">2 piece - Dry-Cleaned &amp; Pressed</div><span class="price">$10.95</span></div>
    <div class="item tall">Women Evening/<br>Formal Dress - From:<div class="sub">Subject to surcharge (beads, etc)</div><span class="price">$15.99</span></div>
    <div class="item">Men's Shirt <span class="sub">(100% cotton)</span><div class="sub">Laundered &amp; Pressed</div><span class="price">$2.99</span></div>
    <div class="item">Men Business Shirt<div class="sub">Dry-Cleaned &amp; Pressed</div><span class="price">$4.50</span></div>
    <div class="item">Men Business Pants<div class="sub">Dry-Cleaned &amp; Pressed</div><span class="price">$4.95</span></div>
  </div>

  <div class="price-col right">
    <div class="item">Men Business Vest<div class="sub">Dry-Cleaned &amp; Pressed</div><span class="price">$4.95</span></div>
    <div class="item">Men Pants/Jeans<div class="sub">Dry-Cleaned &amp; Pressed</div><span class="price">$4.95</span></div>
    <div class="item">Men Suit<div class="sub">2-Piece - Dry-Cleaned &amp; Pressed</div><span class="price">$10.95</span></div>
    <div class="item">3 piece suit<div class="sub">Dry-Cleaned &amp; Pressed</div><span class="price">$15.95</span></div>
    <div class="item">Ties<div class="sub">Dry-Cleaned &amp; Pressed</div><span class="price">$3.95</span></div>
    <div class="item">Sports Coat/Jacket<div class="sub">Dry-Cleaned &amp; Pressed</div><span class="price">$6.95</span></div>
    <div class="item">Men Guayabera<div class="sub">Laundered and Pressed</div><span class="price">$6.99</span></div>
    <div class="item special">LAW ENFORCEMENT<span class="price">$7.99</span><br>OFFICER / MILITARY COMBO SPECIAL!<br>1 LEO or Military shirt with 1 LEO or<br>Military pair of pants<br>combination - Dry-Cleaned and<br>Pressed - Thank you for your service!</div>
  </div>

  <p class="fine">*Silk, linen or felt items may carry a small surcharge per item.<br>*Beaded or embellished garments may carry a surcharge per garment.</p>
  <div class="more tech">For more info login our website</div>

  <div class="notch"></div>
  <div class="back-foot tech">Call Us Now&nbsp;&nbsp;305-472-1946<span class="sep">|</span>deliveryservice@vorqualin.com</div>
</section>

</body>
</html>
```